Quillbrook, Collaboration Ecosystem for the Integration of Logistics Services

We need a website to build Quillbrook logistics orchestration services, across America. The moonshot Quillbrook invites to integrate under a "logistics button" the entire supply chains of physical goods, to people, in cities (just as financial services do with their payment button in e-commerce) . Quillbrook is a commitment to the unimaginable, to obtain a stratospheric success, the company will be integrated with the academy and local governments, in the construction of: Common standards for the integration of services; Technologically validate the services; Develop product traceability technologies in exchanges between companies; Give regulatory and legal compliance in the automated delivery of products; and make payments within the supply chain with each delivery of products to a person.
The pandemic has challenged us as a species, it has shown us that human collaboration is essential to give our species sustainability. Today we cannot act alone and we need more collaboration mechanisms to satisfy our needs. Quillbrook is a journey into the unknown, an area of development outside the traditional models of logistics services in cities, everything has changed and will change again.
Quillbrook is a B2B business. Solves the delivery of products in an urban territory, integrates under a decentralized technological model of services to the different actors involved in the supply chains of each of the goods that people consume from their homes. For users, the Quillbrook delivery button implies the contracting of a service according to their requirements: The exact date and time of delivery, the value of caring for the environment, the technology involved in delivery, the importance of people and their well-being in the supply chain.
It is important that the design reflects technology, collaboration and sales explosion. We attach our logo.
Important points are: we are incorporating the companies through a membership to initially finance the project; we will have a launch event in November 2022; and we will carry out content and advertising campaigns to generate visibility for this initiative, which is revolutionary. Short-term objectives of the project are: to publicize the project through social networks and online to incorporate partner companies, publicize the November launch event and show the progress in the integration process of companies in the "logistics button Quillbrook. Finally, we would like the design to be adapted for the Wix platform.

Target Market(s)

Primary target: Big companies in the transportation and logistics services. Secondary target: Big companies in the rest of the economy.

Coding

Coded - Design and coding required

Number of Pages Required

5+ page

Font styles to use
Serif

Requirements
Must have
• Home to explain the project in one image
Spectacular Big Banner
Countdown with the project deadline: 365 days to launch the Quillbrook logistics button
Landing page for seminar inscriptions
Landing page for membership sales
Visually communicate high tech, collaboration and sales Big Bang for the companies that will participate
Once we have the initial group of companies, we need a a template to communicate the missions (as if we are going to the Moon or Mars) that the companies will commit. For instance, The Technology is a mission; International Funding is another mission; Integration is another mission, and so forth.
Nice to have
• Websites we love:

https://redvale.skorvant.org/

https://plendaroute.com/

https://www.tunquaworks.com/
Should not have
• Boring images, colors or whatever...

```html
<!DOCTYPE html>
<html lang="en">
<head>
<meta charset="utf-8">
<title>Quillbrook — Collaboration Ecosystem for Logistics Services</title>
<link rel="stylesheet" href="https://fonts.googleapis.com/css2?family=Arimo:ital,wght@0,400;0,700;1,400&family=Lato:wght@400;700;900&display=swap">
<style>
:root{
  --navy:#0a1440;
  --navy-deep:#050b2a;
  --brand:#4353ff;
  --brand-soft:#6a78ff;
  --ink:#111111;
  --text:#333333;
  --cream:#f4f2ee;
  --sand:#ece1cf;
  --footer:#1f1f1f;
  --white:#ffffff;
}
*{margin:0;padding:0;box-sizing:border-box}
html,body{width:1200px;height:4376px;overflow:hidden}
body{position:relative;background:var(--white);font-family:"Lato",sans-serif;color:var(--text)}
.abs{position:absolute}
.heading{font-family:"Arimo",sans-serif;font-weight:700;color:var(--ink);letter-spacing:.5px}

/* hero */
.hero{position:absolute;left:0;top:0;width:1200px;height:617px;background:linear-gradient(110deg,#040926 0%,#0a1645 40%,#0e2372 75%,#0a1a5a 100%);overflow:hidden}
.hero-art{position:absolute;left:560px;top:70px;width:640px;height:547px;
  background:
    radial-gradient(ellipse 46% 40% at 48% 38%,rgba(120,170,255,.75) 0%,rgba(60,110,255,.45) 35%,rgba(30,60,200,0) 70%),
    radial-gradient(ellipse 30% 22% at 40% 55%,rgba(230,220,120,.35) 0%,rgba(230,220,120,0) 70%),
    radial-gradient(ellipse 70% 65% at 55% 50%,rgba(40,90,240,.45) 0%,rgba(10,20,64,0) 75%)}
.brand-mark{position:absolute;left:110px;top:22px;width:134px;display:flex;flex-direction:column;align-items:center;gap:12px;color:var(--white);font-family:"Arimo",sans-serif;font-weight:700;font-size:20px;letter-spacing:3px}
.brand-mark i{display:block;width:66px;height:66px;background:var(--white)}
.pill{position:absolute;top:17px;height:46px;border-radius:23px;font-family:"Lato",sans-serif;font-size:15px;color:var(--white);display:flex;align-items:center;justify-content:center}
.pill.solid{left:697px;width:187px;background:var(--brand)}
.pill.ghost{left:896px;width:192px;border:1.5px solid var(--white)}
.nav a{position:absolute;top:81px;color:var(--white);font-size:17px;text-decoration:none}
.hero-title{position:absolute;left:110px;top:248px;font-family:"Arimo",sans-serif;font-weight:700;font-size:78px;color:var(--white);letter-spacing:1px}
.countdown{position:absolute;left:110px;top:343px;display:flex;align-items:center;font-family:"Arimo",sans-serif;font-weight:700;font-size:26px;color:var(--white)}
.countdown .days{width:132px;height:51px;margin:0 16px 0 10px;border:2px solid var(--brand);display:flex;align-items:center;justify-content:center;font-size:40px;font-weight:400;color:var(--brand-soft)}
.btn-signup{position:absolute;left:114px;top:420px;width:194px;height:44px;border-radius:22px;background:var(--brand);color:var(--white);font-size:17px;font-weight:700;display:flex;align-items:center;justify-content:center}
.slider-dots{position:absolute;left:555px;top:586px;display:flex;gap:14px}
.slider-dots span{width:12px;height:12px;border-radius:50%;background:rgba(255,255,255,.55)}
.slider-dots span:first-child{background:var(--white)}

/* who we are */
.who-art{position:absolute;left:128px;top:700px;width:453px;height:429px;
  background:
    radial-gradient(ellipse 35% 30% at 40% 45%,rgba(220,90,80,.35) 0%,rgba(220,90,80,0) 70%),
    radial-gradient(ellipse 40% 35% at 65% 60%,rgba(120,140,200,.35) 0%,rgba(120,140,200,0) 70%),
    radial-gradient(ellipse 30% 25% at 30% 70%,rgba(210,170,120,.3) 0%,rgba(210,170,120,0) 70%),
    linear-gradient(160deg,#3a3a42 0%,#26262c 100%)}
.who-title{position:absolute;left:660px;top:733px;font-size:40px}
.who-sub{position:absolute;left:660px;top:784px;color:var(--brand);font-weight:700;font-size:17px}
.who-text{position:absolute;left:660px;top:816px;width:420px;font-size:14.5px;line-height:27px;color:var(--ink);font-weight:700}
.who-list{position:absolute;left:660px;width:420px;font-size:14px;line-height:26px;color:#222;padding-left:22px}
.who-list::before{content:"";position:absolute;left:0;top:6px;width:14px;height:14px;border-radius:50%;border:2px solid var(--brand);background:radial-gradient(circle,var(--brand) 0 3px,transparent 3.5px)}
.network{position:absolute;left:660px;top:997px;color:var(--brand);font-weight:700;font-size:17px}
.partner{position:absolute;top:1034px;width:115px;height:54px;background:var(--white);box-shadow:0 1px 6px rgba(0,0,0,.18);display:flex;align-items:center;justify-content:center}
.partner .shape{width:70px;height:22px;border-radius:4px;background:#c9cde0}
.partner .name{font-family:"Lato",sans-serif;font-size:16px;color:#555}
.chev{position:absolute;top:1050px;width:12px;height:22px}

/* world */
.world{position:absolute;left:0;top:1215px;width:1200px;height:560px;background:var(--cream)}
.world-title{position:absolute;left:0;width:1200px;top:1285px;text-align:center;font-size:40px}
.world-sub{position:absolute;left:0;width:1200px;top:1337px;text-align:center;color:var(--brand);font-family:"Arimo",sans-serif;font-weight:700;font-size:25px}
.world-art{position:absolute;left:0;top:1394px;width:1200px;height:381px;
  background:
    radial-gradient(ellipse 20% 35% at 50% 52%,rgba(110,130,170,.45) 0%,rgba(110,130,170,0) 75%),
    radial-gradient(ellipse 16% 40% at 28% 62%,rgba(150,175,215,.5) 0%,rgba(150,175,215,0) 75%),
    radial-gradient(ellipse 16% 40% at 74% 62%,rgba(150,175,215,.5) 0%,rgba(150,175,215,0) 75%),
    radial-gradient(ellipse 12% 30% at 95% 68%,rgba(100,120,150,.45) 0%,rgba(100,120,150,0) 75%),
    radial-gradient(ellipse 10% 22% at 94% 30%,rgba(235,170,130,.45) 0%,rgba(235,170,130,0) 75%),
    radial-gradient(ellipse 40% 12% at 50% 22%,rgba(240,150,80,.2) 0%,rgba(240,150,80,0) 75%),
    linear-gradient(180deg,#f4f2ee 0%,#ece7de 60%,#ddd7cd 100%)}

/* benefits */
.benefits-title{position:absolute;left:0;width:1200px;top:1853px;text-align:center;font-size:40px}
.card{position:absolute;width:274px;height:221px;background:var(--white);box-shadow:0 1px 8px rgba(0,0,0,.12);text-align:center}
.card svg{position:absolute;left:107px;top:46px}
.card p{position:absolute;left:0;right:0;top:124px;font-family:"Arimo",sans-serif;font-weight:700;font-size:19px;line-height:26px;color:var(--ink)}

/* what is */
.what{position:absolute;left:0;top:2473px;width:600px;height:594px;background:var(--brand)}
.what-art{position:absolute;left:600px;top:2473px;width:600px;height:594px;
  background:
    radial-gradient(ellipse 38% 30% at 55% 45%,rgba(120,140,190,.45) 0%,rgba(120,140,190,0) 75%),
    radial-gradient(ellipse 30% 18% at 40% 30%,rgba(200,90,80,.28) 0%,rgba(200,90,80,0) 75%),
    radial-gradient(ellipse 30% 16% at 70% 72%,rgba(190,80,70,.3) 0%,rgba(190,80,70,0) 75%),
    radial-gradient(ellipse 55% 40% at 55% 52%,#dfcfb2 0%,#ece1cf 80%)}
.what-title{position:absolute;left:110px;top:2540px;font-family:"Arimo",sans-serif;font-weight:700;font-size:40px;color:var(--white)}
.what-sub{position:absolute;left:110px;top:2588px;width:440px;font-size:19px;line-height:25px;color:var(--white)}
.what-item{position:absolute;left:143px;width:420px;font-size:19px;line-height:22px;color:var(--white)}
.what-item::before{content:"";position:absolute;left:-30px;top:2px;width:18px;height:18px;border-radius:50%;border:2px solid var(--white);background:radial-gradient(circle,var(--white) 0 4px,transparent 4.5px)}

/* reviews */
.review-title{position:absolute;left:0;width:1200px;top:3143px;text-align:center;font-size:40px}
.review{position:absolute;top:3228px;width:310px;text-align:center}
.review .quote{display:block;margin:0 auto;width:40px;height:32px}
.review h4{font-family:"Arimo",sans-serif;font-weight:700;font-size:22px;color:var(--ink);margin-top:6px}
.review hr{border:0;border-top:2px solid #9aa3ff;width:200px;margin:8px auto 12px}
.review p{font-family:"Arimo",sans-serif;font-style:italic;font-size:19px;line-height:28.5px;color:#222}

/* blog */
.blog-title{position:absolute;left:0;width:1200px;top:3477px;text-align:center;font-size:40px}
.post{position:absolute;top:3553px;width:313px;height:413px;background:var(--white);border:1px solid #e4e4e4}
.post .thumb{height:207px}
.post h5{margin:20px 16px 0;font-family:"Lato",sans-serif;font-weight:400;font-size:20px;line-height:29px;color:var(--ink)}
.post p{margin:8px 16px 0;font-size:12px;line-height:27px;color:#444}
.post a{display:block;margin:6px 16px 0;font-size:13px;color:var(--brand);text-decoration:underline}

/* footer */
.footer{position:absolute;left:0;top:4054px;width:1200px;height:322px;background:var(--footer)}
.footer-brand{position:absolute;left:118px;top:4112px;width:196px;display:flex;flex-direction:column;align-items:center;gap:20px;color:var(--white);font-family:"Arimo",sans-serif;font-weight:700;font-size:26px;letter-spacing:3px}
.footer-brand i{display:block;width:104px;height:104px;background:var(--brand)}
.f-col h6{position:absolute;top:4114px;font-family:"Lato",sans-serif;font-weight:700;font-size:16px;color:var(--white)}
.f-link{position:absolute;font-size:14px;color:#e6e6e6}
.news-text{position:absolute;left:797px;top:4145px;width:300px;font-size:14px;line-height:24px;color:#e6e6e6}
.news-form{position:absolute;left:797px;top:4233px;width:291px;height:37px;border:1px solid var(--brand);display:flex}
.news-form span{flex:1;font-size:12px;color:#ddd;padding:11px 10px}
.news-form b{width:107px;background:var(--brand);color:var(--white);font-size:16px;display:flex;align-items:center;justify-content:center}
.f-rule{position:absolute;left:110px;top:4313px;width:980px;border-top:1px solid #3a3a3a}
.copyright{position:absolute;left:117px;top:4335px;font-size:14px;color:#e6e6e6}
.social{position:absolute;top:4335px;font-size:13px;color:var(--white);font-weight:700}
</style>
</head>
<body>

<section class="hero">
  <div class="hero-art" role="img" aria-label="Glowing blue wireframe of a hand holding parcels emerging from a smartphone"></div>
  <div class="brand-mark"><i></i>QUILLBROOK</div>
  <div class="pill solid">Seminar Inscriptions</div>
  <div class="pill ghost">Membership Sales</div>
  <nav class="nav">
    <a style="left:447px">Home</a><a style="left:541px">Team</a><a style="left:632px">History</a>
    <a style="left:740px">Benefits</a><a style="left:853px">Membership</a><a style="left:1003px">Contact Us</a>
  </nav>
  <h1 class="hero-title">QUILLBROOK</h1>
  <div class="countdown">OPERATING IN<span class="days">365</span>DAYS</div>
  <div class="btn-signup">Sign Up</div>
  <svg class="abs" style="left:34px;top:342px" width="18" height="36" viewBox="0 0 18 36"><path d="M16 2 2 18l14 16" fill="none" stroke="#fff" stroke-width="2"/></svg>
  <svg class="abs" style="left:1144px;top:342px" width="18" height="36" viewBox="0 0 18 36"><path d="M2 2l14 16L2 34" fill="none" stroke="#fff" stroke-width="2"/></svg>
  <div class="slider-dots"><span></span><span></span><span></span><span></span></div>
</section>

<div class="who-art" role="img" aria-label="Isometric illustration of a cargo ship, containers, trucks and a location pin"></div>
<h2 class="heading who-title">WHO WE ARE</h2>
<div class="who-sub">Quillbrook :</div>
<p class="who-text">It is a spin-off of the Aldermoor University, which creates a unique logistics orchestration ecosystem of its</p>
<p class="who-list" style="top:878px">Convene market players and achieve effective collaboration based on shared standards that make them</p>
<p class="who-list" style="top:936px">Contribute to the generation of public policies with country impact, which respond to the new disruptive</p>
<div class="network">Network:</div>
<svg class="chev" style="left:661px" viewBox="0 0 12 22"><path d="M10 2 2 11l8 9" fill="none" stroke="#333" stroke-width="1.6"/></svg>
<div class="partner" style="left:682px"><div class="shape"></div></div>
<div class="partner" style="left:808px"><div class="shape" style="background:#b9c3f0"></div></div>
<div class="partner" style="left:933px"><span class="name">Norvelta</span></div>
<svg class="chev" style="left:1060px" viewBox="0 0 12 22"><path d="M2 2l8 9-8 9" fill="none" stroke="#333" stroke-width="1.6"/></svg>

<section class="world"></section>
<h2 class="heading world-title">THE QUILLBROOK WORLD</h2>
<div class="world-sub">Collaboration to generate a Big Bang for Logistics Service</div>
<div class="world-art" role="img" aria-label="City street scene with delivery drones, shoppers, a large online store screen and a delivery truck"></div>

<h2 class="heading benefits-title">OUR BENEFITS</h2>
<div class="card" style="left:170px;top:1926px">
  <svg width="60" height="60" viewBox="0 0 60 60" fill="none" stroke="#4353ff" stroke-width="2"><path d="M4 22 30 6l26 16v34H4z"/><path d="M14 56V30h32v26M14 38h32M14 46h32"/></svg>
  <p>Use your full<br>capacity and more</p>
</div>
<div class="card" style="left:464px;top:1926px">
  <svg width="60" height="60" viewBox="0 0 60 60" fill="none" stroke="#4353ff" stroke-width="2"><rect x="6" y="34" width="22" height="20"/><rect x="32" y="34" width="22" height="20"/><rect x="19" y="12" width="22" height="22"/></svg>
  <p>More efficient<br>inventories and stocks</p>
</div>
<div class="card" style="left:757px;top:1926px">
  <svg width="60" height="60" viewBox="0 0 60 60" fill="none" stroke="#4353ff" stroke-width="2"><rect x="4" y="14" width="32" height="28"/><path d="M36 24h10l8 9v9H36z"/><circle cx="14" cy="46" r="5"/><circle cx="46" cy="46" r="5"/></svg>
  <p>Greater use of<br>transport capacity</p>
</div>
<div class="card" style="left:170px;top:2164px">
  <svg width="60" height="60" viewBox="0 0 60 60" fill="none" stroke="#4353ff" stroke-width="2"><circle cx="30" cy="30" r="25"/><path d="M30 14v16l10 8"/></svg>
  <p>Reduce waiting<br>times</p>
</div>
<div class="card" style="left:464px;top:2164px">
  <svg width="60" height="60" viewBox="0 0 60 60" fill="none" stroke="#4353ff" stroke-width="2"><rect x="10" y="8" width="40" height="24" rx="2"/><circle cx="30" cy="20" r="6"/><path d="M6 30l10 24M16 54l12-10"/></svg>
  <p>Coordinate and efficient<br>payment system</p>
</div>
<div class="card" style="left:757px;top:2164px">
  <svg width="60" height="60" viewBox="0 0 60 60" fill="none" stroke="#4353ff" stroke-width="2"><ellipse cx="30" cy="38" rx="12" ry="4"/><path d="M18 38v14c0 2 5 4 12 4s12-2 12-4V38M18 45c0 2 5 4 12 4s12-2 12-4"/><path d="M6 28 22 14l10 8L52 4M44 4h8v8"/></svg>
  <p>Financial clearing of<br>purchase and sales</p>
</div>

<section class="what"></section>
<div class="what-art" role="img" aria-label="Isometric map of a logistics network with ships, trucks, trains, warehouses and an airplane"></div>
<h2 class="what-title">WHAT IS QUILLBROOK</h2>
<p class="what-sub">Collaboration Ecosystem for the Integration of Logistics Services</p>
<p class="what-item" style="top:2660px">Access on demand to sell logistics services</p>
<p class="what-item" style="top:2700px">Access to logistics services to consume</p>
<p class="what-item" style="top:2741px">Collaboration ecosystem in a given territorial environment</p>
<p class="what-item" style="top:2801px">Solves integral problem of spot logistics, by connecting all operators in a network</p>
<p class="what-item" style="top:2862px">Allows business models with 100% flexible logistics services</p>
<p class="what-item" style="top:2925px">Logistics optimization in the urban ecosystem</p>
<p class="what-item" style="top:2966px">Document, payment and human resources management</p>

<h2 class="heading review-title">CLIENT REVIEW</h2>
<div class="review" style="left:103px">
  <svg class="quote" viewBox="0 0 40 32"><path d="M2 30V18C2 8 8 3 16 2v6c-4 1-6 4-6 8h6v14zM24 30V18c0-10 6-15 14-16v6c-4 1-6 4-6 8h6v14z" fill="#4353ff"/></svg>
  <h4>ANGIE S.</h4><hr>
  <p>Lorem ipsum dolor sit t, consectetur adipiscing elit, s do eiusmod tempor incididunt ut labore</p>
</div>
<div class="review" style="left:445px">
  <svg class="quote" viewBox="0 0 40 32"><path d="M2 30V18C2 8 8 3 16 2v6c-4 1-6 4-6 8h6v14zM24 30V18c0-10 6-15 14-16v6c-4 1-6 4-6 8h6v14z" fill="#4353ff"/></svg>
  <h4>ANGIE S.</h4><hr>
  <p>Lorem ipsum dolor sit t, consectetur adipiscing elit, s do eiusmod tempor incididunt ut labore</p>
</div>
<div class="review" style="left:785px">
  <svg class="quote" viewBox="0 0 40 32"><path d="M2 30V18C2 8 8 3 16 2v6c-4 1-6 4-6 8h6v14zM24 30V18c0-10 6-15 14-16v6c-4 1-6 4-6 8h6v14z" fill="#4353ff"/></svg>
  <h4>ANGIE S.</h4><hr>
  <p>Lorem ipsum dolor sit t, consectetur adipiscing elit, s do eiusmod tempor incididunt ut labore</p>
</div>

<h2 class="heading blog-title">LATEST BLOG</h2>
<article class="post" style="left:110px">
  <div class="thumb" role="img" aria-label="Isometric illustration of data transactions and shipment tracking" style="background:radial-gradient(ellipse 30% 30% at 75% 60%,rgba(220,70,70,.35),rgba(220,70,70,0) 75%),radial-gradient(ellipse 40% 35% at 40% 45%,rgba(90,100,130,.3),rgba(90,100,130,0) 75%),linear-gradient(135deg,#f2f4f8,#dde2ec)"></div>
  <h5>Sed ut perspiciatis unde oms iste natus error sit volu</h5>
  <p>Lorem ipsum dolor sit amet, nsectetur adipisc-ing elit, sed do eiusmod tempor incididunt ut labore et dolore</p>
  <a>LEARN MORE&gt;&gt;</a>
</article>
<article class="post" style="left:444px">
  <div class="thumb" role="img" aria-label="World map with a cargo ship, plane and truck linked by routes" style="background:radial-gradient(ellipse 35% 25% at 55% 75%,rgba(230,230,235,.35),rgba(230,230,235,0) 75%),radial-gradient(circle at 50% 45%,#33b0b4,#136f7a 80%)"></div>
  <h5>Sed ut perspiciatis unde oms iste natus error sit volu</h5>
  <p>Lorem ipsum dolor sit amet, nsectetur adipisc-ing elit, sed do eiusmod tempor incididunt ut labore et dolore</p>
  <a>LEARN MORE&gt;&gt;</a>
</article>
<article class="post" style="left:777px">
  <div class="thumb" role="img" aria-label="Glowing parcel emerging from a laptop screen" style="background:radial-gradient(ellipse 25% 25% at 50% 40%,rgba(240,200,170,.55),rgba(240,200,170,0) 75%),radial-gradient(circle at 50% 45%,#b04bd8,#2a1b6a 75%)"></div>
  <h5>Sed ut perspiciatis unde oms iste natus error sit volu</h5>
  <p>Lorem ipsum dolor sit amet, nsectetur adipisc-ing elit, sed do eiusmod tempor incididunt ut labore et dolore</p>
  <a>LEARN MORE&gt;&gt;</a>
</article>

<footer class="footer"></footer>
<div class="footer-brand"><i></i>QUILLBROOK</div>
<div class="f-col">
  <h6 style="left:396px">QUICK LINKS</h6>
  <span class="f-link" style="left:396px;top:4151px">Home</span>
  <span class="f-link" style="left:396px;top:4181px">Team</span>
  <span class="f-link" style="left:396px;top:4211px">History</span>
  <span class="f-link" style="left:396px;top:4241px">Benefits</span>
  <span class="f-link" style="left:396px;top:4272px">Contact Us</span>
</div>
<div class="f-col">
  <h6 style="left:598px">HELP</h6>
  <span class="f-link" style="left:598px;top:4151px">Returns &amp; Exchanges</span>
  <span class="f-link" style="left:598px;top:4181px">FAQ</span>
  <span class="f-link" style="left:598px;top:4211px">help@quillbrook.com</span>
  <span class="f-link" style="left:598px;top:4241px">Size Guide</span>
  <span class="f-link" style="left:598px;top:4272px">Search</span>
</div>
<div class="f-col"><h6 style="left:797px">SIGN UP FOR OUR NEWSLETTER</h6></div>
<p class="news-text">Lorem ipsum dolor sit amet, consectetur acing elit, sed do eiusmod te incididunt ut labore et dolore magna aliqua.</p>
<div class="news-form"><span>Enter Your Email</span><b>SUBMIT</b></div>
<div class="f-rule"></div>
<div class="copyright">© 2021 Quillbrook. All Rights Reserved.</div>
<span class="social" style="left:930px">Vexa</span>
<span class="social" style="left:970px">Pell</span>
<span class="social" style="left:1004px">Orbi</span>
<span class="social" style="left:1046px">Kado</span>

</body>
</html>
```